ice cream shop needs flavor of the month poster

we need an A3 size poster design for the flavor of the month . we will provide you 2 ice cream images to choose from one in a cone which we personally prefer and the other one in a cup . we will also provide you our colors pantone and patterns if you would like to use it. the design should focus on the ice cream image and it should has the title of flavor of the moth and the name of the ice cream mix which is ( Samir Velvo ice cream mix) .

Target Market(s)

families and 18-25

Industry/Entity Type

Cafe

Font styles to use
Other font styles liked:
• arial

Colors
eea4c8
fbf289
f68e4e
abd036

Requirements
Must have
• logo small size
• name of the mix (samir velvo ice cream mix)
• title ( Flavor of the month )
Nice to have
• keep it simple

```html
<!DOCTYPE html>
<html lang="en">
<head>
<meta charset="utf-8">
<title>Flavor of the month poster</title>
<link rel="stylesheet" href="https://fonts.googleapis.com/css2?family=Archivo+Black&family=Fredoka:wght@500&family=Arimo&display=swap">
<style>
  :root {
    --stage: #1f1f22;
    --pink: #eea4c8;
    --pink-deep: #ec8fbd;
    --pink-soft: #fbe3ee;
    --paper: #f1f3f5;
    --brown: #5a3227;
    --yellow: #fbf289;
    --cream: #efe6da;
    --biscuit: #c98a4f;
    --white: #ffffff;
  }
  * { margin: 0; padding: 0; box-sizing: border-box; }
  html, body { width: 800px; height: 1200px; overflow: hidden; }
  body { background: var(--stage); position: relative; }

  .poster {
    position: absolute; left: 0; top: 34px;
    width: 800px; height: 1131px; overflow: hidden;
    background: var(--paper);
  }
  .poster__rays { position: absolute; inset: 0; width: 800px; height: 1131px; }

  .brand {
    position: absolute; left: 34px; top: 46px;
    display: flex; align-items: center; gap: 8px;
  }
  .brand__dot {
    width: 26px; height: 26px; border-radius: 50%;
    background: var(--yellow); border: 2px solid var(--brown);
  }
  .brand__name {
    font-family: "Arimo", Arial, sans-serif; font-size: 13px;
    color: var(--brown); line-height: 1.15; width: 80px;
  }

  .headline {
    position: absolute; left: 0; right: 0; top: 40px;
    text-align: center; color: var(--brown);
    font-family: "Archivo Black", Arial, sans-serif;
  }
  .headline__main { display: block; font-size: 116px; line-height: 1; letter-spacing: -1px; }
  .headline__sub { display: block; font-size: 55px; line-height: 1; margin-top: 6px; }

  .hero-photo {
    position: absolute; left: 86px; top: 252px;
    width: 600px; height: 812px;
    border-radius: 260px 260px 20px 20px;
    background: radial-gradient(ellipse at 55% 30%, var(--cream) 0%, #e3cfb6 45%, var(--biscuit) 100%);
  }

  .flavor-tag {
    position: absolute; left: 140px; top: 830px;
    width: 520px; height: 150px;
    transform: rotate(-7deg);
    background: var(--yellow);
    border: 5px solid var(--brown);
    display: flex; flex-direction: column; align-items: center; justify-content: center;
    font-family: "Fredoka", Arial, sans-serif; font-weight: 500; color: var(--brown);
  }
  .flavor-tag__name { font-size: 76px; line-height: 0.95; }
  .flavor-tag__kind { font-size: 44px; line-height: 1; }

  .footer-band {
    position: absolute; left: 0; bottom: 0; width: 800px; height: 67px;
    background: var(--pink-deep);
    display: flex; align-items: center; justify-content: center;
    font-family: "Arimo", Arial, sans-serif; font-size: 20px;
    letter-spacing: 5px; color: var(--white);
  }
</style>
</head>
<body>
  <main class="poster">
    <svg class="poster__rays" viewBox="0 0 800 1131" aria-hidden="true">
      <defs>
        <linearGradient id="rayLeft" x1="0" y1="0" x2="0" y2="1">
          <stop offset="0" stop-color="#fdf1f6"/>
          <stop offset="1" stop-color="#ee9cc6"/>
        </linearGradient>
        <linearGradient id="rayRight" x1="0" y1="0" x2="0" y2="1">
          <stop offset="0" stop-color="#fdf1f6"/>
          <stop offset="1" stop-color="#ee9cc6"/>
        </linearGradient>
      </defs>
      <rect width="800" height="1131" fill="url(#rayLeft)"/>
      <polygon points="22,0 778,0 560,1131 250,1131" fill="var(--paper)"/>
      <polygon points="0,300 0,1131 250,1131" fill="url(#rayLeft)" opacity="0.6"/>
      <polygon points="800,280 800,1131 560,1131" fill="url(#rayRight)" opacity="0.6"/>
    </svg>

    <div class="brand">
      <span class="brand__dot"></span>
      <span class="brand__name">Glacier Stone Creamery</span>
    </div>

    <h1 class="headline">
      <span class="headline__main">Flavor</span>
      <span class="headline__sub">of the month</span>
    </h1>

    <div class="hero-photo" role="img" aria-label="Waffle cone with two scoops of biscuit ice cream, caramel drizzle, biscuit crumbs and a whole spiced biscuit"></div>

    <div class="flavor-tag">
      <span class="flavor-tag__name">samir velvo</span>
      <span class="flavor-tag__kind">ice cream mix</span>
    </div>

    <footer class="footer-band">www.glacierstone.com</footer>
  </main>
</body>
</html>
```